Harborline Crest Insurance Services

we are a high end insurance agency we specialize on Auto | Home | Business | Life looking for something professional and luxuries at the same time. if you guys need anything else please let me know.

Auto | Home | Business | Life must be under logo on the back with black background.

i want the back part to be black with our gold logo on it.

Target Market(s)

Auto | Home | Business | Life

Industry/Entity Type

Insurance Broker

Contact Information for Business Card

My logo is gold so a black in the back would be nice.

Font styles to use
Serif

Colors
000000

Requirements
Must have
• Big logo on the back with black background.

```html
<!DOCTYPE html>
<html lang="en">
<head>
<meta charset="utf-8">
<title>Harborline Crest Insurance Services – Business Card</title>
<link href="https://fonts.googleapis.com/css2?family=Alegreya+SC:wght@500&family=Open+Sans:wght@400&display=swap" rel="stylesheet">
<style>
  :root {
    --stage-top: #a3a3a3;
    --stage-bottom: #8a8a8a;
    --ink-black: #0b0b0b;
    --gold: #f2c22e;
    --gold-light: #fbd146;
    --gold-deep: #eebd2a;
    --text-dark: #141414;
    --text-light: #dcdcdc;
  }
  * { box-sizing: border-box; margin: 0; padding: 0; }
  html, body { width: 1200px; height: 900px; overflow: hidden; }
  body {
    background: linear-gradient(to bottom, var(--stage-top), var(--stage-bottom));
    position: relative;
    font-family: "Open Sans", Arial, sans-serif;
  }
  .card {
    position: absolute;
    top: 306px;
    width: 440px;
    height: 271px;
    border-radius: 10px;
    overflow: hidden;
    box-shadow: 0 1px 3px rgba(0,0,0,.25);
  }
  /* Front */
  .card-front { left: 149px; background: linear-gradient(to bottom, var(--gold-light), var(--gold-deep)); }
  .front-header {
    position: absolute; left: 0; top: 0; width: 100%; height: 117px;
    background: var(--ink-black);
  }
  .brand-name {
    position: absolute; left: 22px; top: 38px;
    font-family: "Alegreya SC", Georgia, serif; font-weight: 500;
    color: var(--gold); font-size: 22px; line-height: 24px;
  }
  .holder { position: absolute; right: 23px; top: 46px; text-align: right; }
  .holder-name {
    font-family: "Alegreya SC", Georgia, serif; font-weight: 500;
    color: var(--gold); font-size: 17px; line-height: 20px; letter-spacing: .3px;
  }
  .holder-title { color: var(--text-light); font-size: 12px; line-height: 16px; }
  .contact-list { position: absolute; left: 23px; top: 146px; list-style: none; }
  .contact-list li {
    display: flex; align-items: center; gap: 6px;
    font-size: 12px; line-height: 16px; color: var(--text-dark);
  }
  .contact-list svg { width: 10px; height: 10px; fill: var(--text-dark); }
  .address { position: absolute; left: 22px; top: 214px; font-size: 12px; line-height: 17px; color: var(--text-dark); }
  .emboss-area {
    position: absolute; right: 0; top: 117px; width: 200px; height: 154px;
    background: radial-gradient(ellipse at 50% 45%, rgba(255,230,120,.45), rgba(255,230,120,0) 65%);
  }
  /* Back */
  .card-back {
    left: 608px;
    background: radial-gradient(ellipse at 50% 40%, #1a1a1a, var(--ink-black) 75%);
    text-align: center;
  }
  .back-mark {
    position: absolute; left: 50%; top: 56px; width: 70px; height: 70px;
    margin-left: -35px; border-radius: 50%; background: var(--gold);
  }
  .back-brand {
    position: absolute; left: 0; right: 0; top: 166px;
    font-family: "Alegreya SC", Georgia, serif; font-weight: 500;
    color: var(--gold); font-size: 24px; line-height: 26px;
  }
  .service-lines {
    position: absolute; left: 0; right: 0; top: 224px;
    font-family: "Alegreya SC", Georgia, serif; font-weight: 500;
    color: var(--gold); font-size: 14px; letter-spacing: .3px;
    display: flex; justify-content: center; gap: 6px;
  }
  .service-lines span::before {
    content: ""; display: inline-block; width: 6px; height: 6px; border-radius: 50%;
    background: var(--gold); margin-right: 4px; vertical-align: 2px;
  }
</style>
</head>
<body>
  <section class="card card-front">
    <header class="front-header">
      <div class="brand-name">Harborline Crest<br>Insurance Services</div>
      <div class="holder">
        <div class="holder-name">Marcus Hale</div>
        <div class="holder-title">Managing Director</div>
      </div>
    </header>
    <ul class="contact-list">
      <li><svg viewBox="0 0 10 10"><path d="M3 0h4a1 1 0 0 1 1 1v8a1 1 0 0 1-1 1H3a1 1 0 0 1-1-1V1a1 1 0 0 1 1-1zm0 1.5v6h4v-6z"/></svg>044-555 210 348</li>
      <li><svg viewBox="0 0 10 10"><path d="M0 3q5-3 10 0v1.5H7.5V3.5Q5 2.5 2.5 3.5v1H0zM2.5 5h5l1.5 4H1z"/></svg>044-555 210 348</li>
      <li><svg viewBox="0 0 10 10"><path d="M0 2h10v6H0zm1 .8 4 3 4-3z"/></svg>info@harborlinecrest.com</li>
      <li><svg viewBox="0 0 10 10"><circle cx="5" cy="5" r="5"/><path d="M1 5h8M5 1c-2 2-2 6 0 8M5 1c2 2 2 6 0 8" stroke="#f6c93a" stroke-width=".8" fill="none"/></svg>www.harborlinecrest.com</li>
    </ul>
    <p class="address">48 Quayside Row, Suite 5<br>Port Elland, 204519.</p>
    <div class="emboss-area" role="img" aria-label="Faint embossed emblem area"></div>
  </section>

  <section class="card card-back">
    <div class="back-mark"></div>
    <div class="back-brand">Harborline Crest<br>Insurance Services</div>
    <div class="service-lines"><span>Auto</span><span>Home</span><span>Business</span><span>Life</span></div>
  </section>
</body>
</html>
```